Very Simple Web Redesign Project - Using Photoshop

Required is a very simple website home page redesign for the following site: http://www.kestrelslateworks.com.au/
I require this as a Photoshop design.
The basic look and feel of the site needs to remain.
Specifically the colours don't need to be changed.
The positioning of the site is currently correct for the target market.
The site does not need to be made super slick looking. Just upgraded to a new version.
The current text can all be used.
The only menus necessary are a horizontal menu at the top, and a simple horizontal text menu at the bottom of the page. Do NOT retain the vertical menu on the home page (having the items "Our Gallery", "Our Services", "Enquire Now").
Give the horizontal menu the following items:
Home | Slate Roof Repairs | Slate Reroofing | Slate Roof Benefits | Other Services | Photo Gallery | FAQ's | Free Quote | Contact Us
The picture of the house at the top RHS of the page needs to be reduced in size by approx 50% and moved to the top LHS of the page.
Please place the following text into the top of the page:
"Call Now: 0427 618 302"
Keep the four pictures on the home page layout. Some larger images attached.
Thanks,
Ned
Updates
Hi,
Thanks for all the designs.
I am working with my client to get which one they like the most.
Thanks,
Ned

```html
<!DOCTYPE html>
<html lang="en">
<head>
<meta charset="utf-8">
<title>Kestrel Slateworks</title>
<link href="https://fonts.googleapis.com/css2?family=Arimo:wght@400;700&family=Roboto:wght@300;400&display=swap" rel="stylesheet">
<style>
:root{
  --green-dark:#1f4a0f;
  --green-mid:#3f7f1e;
  --nav-bg:#27550f;
  --hero-bg:#dfe0a6;
  --body-bg:#f3f1e2;
  --footer-bg:#162e08;
  --text-dark:#1a1a1a;
  --text-green:#2b5a0e;
  --phone-yellow:#f2e021;
  --rule:#cfcfc0;
}
*{margin:0;padding:0;box-sizing:border-box}
html,body{width:1180px;height:1200px;overflow:hidden}
body{font-family:"Arimo",Arial,sans-serif;background:var(--body-bg);position:relative;color:var(--text-dark)}
.header{position:absolute;left:0;top:0;width:1180px;height:146px;
  background:radial-gradient(ellipse 420px 120px at 340px 40px,#8fc03c 0%,transparent 70%),linear-gradient(180deg,#2e6a14 0%,var(--green-mid) 45%,#3b7a1b 100%);}
.header::before{content:"";position:absolute;left:0;top:0;width:100%;height:30px;background:linear-gradient(180deg,#1e4a0c,rgba(30,74,12,0))}
.top-links{position:absolute;right:95px;top:7px;font-family:"Roboto",sans-serif;font-size:14px;color:#fff}
.top-links span{margin:0 9px}
.brand{position:absolute;left:112px;top:60px;display:flex;align-items:center;gap:14px}
.brand-mark{width:26px;height:26px;background:#fff}
.brand-name{font-size:40px;font-weight:700;color:#fff;letter-spacing:-0.5px}
.nav{position:absolute;left:0;top:146px;width:1180px;height:60px;background:linear-gradient(180deg,#2e5f14,var(--nav-bg));border-top:1px solid #5e9a32;display:flex;padding-left:72px}
.nav a{font-family:"Roboto",sans-serif;font-weight:300;font-size:16px;color:#fff;text-decoration:none;line-height:58px;padding:0 35px;position:relative}
.nav a+a::before{content:"";position:absolute;left:0;top:15px;height:30px;width:1px;background:#6b9a4a}
.hero{position:absolute;left:0;top:206px;width:1180px;height:391px;background:var(--hero-bg);border-bottom:1px solid #c9c995}
.hero h1{position:absolute;left:110px;top:52px;font-weight:400;font-size:36px;line-height:48px;color:var(--green-dark);letter-spacing:-0.5px}
.hero h1 strong{font-size:42px;font-weight:700}
.hero p{position:absolute;left:109px;top:166px;width:372px;font-family:"Roboto",sans-serif;font-size:14px;line-height:20px;color:var(--text-green)}
.phone{position:absolute;left:109px;top:265px;width:336px;height:62px;border-radius:31px;background:linear-gradient(180deg,#6fae36 0%,#3f8119 50%,#2a6410 51%,#1f5109 100%);border:1px solid #1d4709;display:flex;align-items:center;gap:18px;padding-left:32px}
.phone span{font-size:34px;font-weight:700;color:var(--phone-yellow)}
.gallery{position:absolute;left:522px;top:59px;width:549px;height:279px;background:#fff}
.gallery div{position:absolute}
.ph1{left:5px;top:5px;width:127px;height:129px;background:linear-gradient(#6f7a7a,#9a9ea0)}
.ph2{left:5px;top:144px;width:127px;height:129px;background:linear-gradient(#3e4255,#5a5f70)}
.ph3{left:142px;top:5px;width:149px;height:268px;background:linear-gradient(#6e7e4c,#8a8f95 45%,#d0c9b6 70%,#6aa331)}
.ph4{left:301px;top:5px;width:243px;height:268px;background:linear-gradient(#a7c0dc,#6c6e78 35%,#7c7d84 70%,#b8b8b4)}
.col{position:absolute;top:660px}
.col h2{font-weight:400;font-size:23px;padding-bottom:10px;border-bottom:3px solid #222;color:#111}
.col p{font-family:"Roboto",sans-serif;font-size:12px;line-height:20px;color:#222}
.col-left{left:109px;width:383px}
.col-right{left:520px;width:551px}
.col-left .intro{margin-top:32px}
.checks{list-style:none;margin-top:24px;width:378px}
.checks li{font-family:"Roboto",sans-serif;font-size:12px;height:50px;display:flex;align-items:center;gap:8px;border-bottom:1px solid var(--rule)}
.checks li:last-child{border-bottom:none}
.checks svg{flex:none}
.col-right p{margin-top:32px}
.col-right p+p{margin-top:40px}
.roofline{position:absolute;left:762px;top:1110px;width:308px;height:30px;background:linear-gradient(180deg,rgba(22,46,8,0) 0%,rgba(22,46,8,0.55) 45%,var(--footer-bg) 100%)}
.footer{position:absolute;left:0;top:1140px;width:1180px;height:60px;background:var(--footer-bg);font-size:11px;letter-spacing:0.5px;color:#dfe6c7}
.footer nav{position:absolute;left:108px;top:24px}
.footer nav span{margin:0 10px}
.copy{position:absolute;right:110px;top:24px;font-weight:700}
</style>
</head>
<body>
<header class="header">
  <div class="top-links">Free Quote<span>|</span>Contact Us</div>
  <div class="brand"><div class="brand-mark"></div><div class="brand-name">Kestrel Slateworks</div></div>
</header>
<nav class="nav">
  <a>Home</a><a>Slate Roof Repairs</a><a>Slate Reroofing</a><a>Slate Roof Benefits</a><a>Other Services</a><a>Photo Gallery</a>
</nav>
<section class="hero">
  <h1>Call now and arrange<br>a <strong>free quote</strong></h1>
  <p>We service all inner city suburbs of Sydney roughly covering an area encompassing Gordon to Epping, Mosman to Bondi, Coogee to Kogarah and Kingsgrove to Burwood and Concord</p>
  <div class="phone">
    <svg width="38" height="28" viewBox="0 0 38 28"><path d="M2 9c0-5 34-5 34 0v4h-9v-3H11v3H2z" fill="#f2e021"/><rect x="9" y="13" width="20" height="13" rx="2" fill="#f2e021"/><circle cx="19" cy="19" r="4" fill="#2f6b12"/></svg>
    <span>0427 618 302</span>
  </div>
  <div class="gallery">
    <div class="ph1" role="img" aria-label="Photo of a window set in a slate roof"></div>
    <div class="ph2" role="img" aria-label="Photo of a dormer window on a slate roof"></div>
    <div class="ph3" role="img" aria-label="Photo of a conical slate turret roof"></div>
    <div class="ph4" role="img" aria-label="Photo of a house with a new slate roof"></div>
  </div>
</section>
<section class="col col-left">
  <h2>Why choose Kestrel Slateworks?</h2>
  <p class="intro">At Kestrel Slateworks we provide a variety of services in the upkeep, maintenance and or replacement of your slate and wood shingle roof.</p>
  <ul class="checks">
    <li><svg width="15" height="15"><rect width="15" height="15" fill="#1f3d0c"/><path d="M5 3l6 4.5L5 12z" fill="#fff"/></svg>Lorem ipsum dolor sit amet, consectetur adipisicing</li>
    <li><svg width="15" height="15"><rect width="15" height="15" fill="#1f3d0c"/><path d="M5 3l6 4.5L5 12z" fill="#fff"/></svg>Lorem ipsum dolor sit amet, consectetur adipisicing elit</li>
    <li><svg width="15" height="15"><rect width="15" height="15" fill="#1f3d0c"/><path d="M5 3l6 4.5L5 12z" fill="#fff"/></svg>Lorem ipsum dolor sit amet, consectetur</li>
    <li><svg width="15" height="15"><rect width="15" height="15" fill="#1f3d0c"/><path d="M5 3l6 4.5L5 12z" fill="#fff"/></svg>Lorem ipsum dolor sit amet, consectetur adipisicing</li>
    <li><svg width="15" height="15"><rect width="15" height="15" fill="#1f3d0c"/><path d="M5 3l6 4.5L5 12z" fill="#fff"/></svg>Lorem ipsum dolor sit amet, consectetur adipisicing elit</li>
    <li><svg width="15" height="15"><rect width="15" height="15" fill="#1f3d0c"/><path d="M5 3l6 4.5L5 12z" fill="#fff"/></svg>Lorem ipsum dolor sit amet, consectetur</li>
  </ul>
</section>
<section class="col col-right">
  <h2>Kestrel Slateworks - the Slate Roof Specialists</h2>
  <p>At Kestrel Slateworks we specialize in the upkeep, maintenance, repair and replacement of all types of slate roof as well as wood shingles. We can track down the leak that just won't go away or give your house a complete re-roof. We can also provide all your guttering needs.</p>
  <p>Kestrel Slateworks is a small company and as such we do not have the overheads that larger companies do. Quality work and attention to detail are our trademark.</p>
  <p>All photos on this website consist of work which I have personally done. The above photos provide at a quick glance a reasonable cross section of the type of work I do.</p>
  <p>By clicking on the Photo Gallery link you can see other work including some before and after shots.</p>
  <p>Feel free to call at your earliest convenience to organise an obligation free quote or fill out a form by clicking on the Contact Us link below.</p>
</section>
<div class="roofline" role="img" aria-label="Silhouette of house rooftops above the footer"></div>
<footer class="footer">
  <nav>Home<span>|</span>Legal Disclaimer<span>|</span>Terms of Use<span>|</span>Privacy Policy<span>|</span>FAQ<span>|</span>Sitemap</nav>
  <div class="copy">Copyright © 2011 Kestrel Slateworks.</div>
</footer>
</body>
</html>
```